Medical Clinic Website - New Private Clinic

We have a basic design for a website. Would like it developed in WORDPRESS. the attached JPG shows the page basic design.

Colours and overall design to be similar

MUST BE WORD PRESS and must allow our company to edit at later date. Images must be licenced for use.

The text to be included is:

Medical or GP clinic patients

Medical

1 page

• WORDPRESS and use the attached jpg as a design guide.
• Must be able to allow me to insert link to "slot lantern" in the top LEFT CORNER. a button or similar. The slot lantern designers will help us with this, but it must have the space

```html
<!DOCTYPE html>
<html lang="en">
<head>
<meta charset="utf-8">
<title>Harbour Lane GP</title>
<link rel="stylesheet" href="https://fonts.googleapis.com/css2?family=Questrial&family=Open+Sans:wght@400;600&display=swap">
<style>
  :root {
    --green: #8dc21f;
    --green-dark: #7aae14;
    --blue: #1fa3e0;
    --blue-deep: #1b5e93;
    --navy: #2b4a7a;
    --ink: #4a4f55;
    --white: #ffffff;
    --mist: #e4ebf0;
    --line: #9fb3c4;
  }
  * { box-sizing: border-box; margin: 0; padding: 0; }
  html, body { width: 1200px; height: 2226px; overflow: hidden; background: var(--white); }
  body { font-family: "Questrial", "Century Gothic", sans-serif; color: var(--ink); position: relative; }

  .site-header { position: absolute; left: 0; top: 0; width: 1200px; height: 204px; background: var(--white); }
  .booking-slot {
    position: absolute; left: 66px; top: 75px; width: 250px; height: 60px;
    border: 3px solid var(--line); color: var(--navy);
    font-size: 30px; letter-spacing: 1px; text-transform: uppercase;
    display: flex; align-items: center; justify-content: center;
  }
  .brand { position: absolute; left: 420px; top: 70px; width: 360px; display: flex; align-items: center; justify-content: center; gap: 16px; }
  .brand-mark { width: 26px; height: 26px; background: var(--green); }
  .brand-name { font-size: 44px; color: var(--blue-deep); white-space: nowrap; }
  .header-phone { position: absolute; right: 56px; top: 78px; display: flex; align-items: center; gap: 18px; color: var(--blue); font-size: 42px; }

  .nav-bar { position: absolute; left: 0; top: 204px; width: 1200px; height: 96px; background: var(--green); }
  .menu-toggle { position: absolute; right: 74px; top: 22px; width: 84px; height: 54px; display: flex; flex-direction: column; justify-content: space-between; }
  .menu-toggle span { display: block; height: 10px; background: var(--white); }

  .hero-visual { position: absolute; left: 0; top: 300px; width: 1200px; height: 420px;
    background: linear-gradient(100deg, #b9d4ea 0%, #5aa7dc 35%, #1b8fd6 60%, #cfe3f2 100%); }

  .cta-band { position: absolute; left: 0; top: 720px; width: 1200px; height: 340px; background: var(--green); color: var(--white); }
  .cta-kicker { position: absolute; left: 62px; top: 44px; font-size: 44px; letter-spacing: 2px; }
  .cta-title { position: absolute; left: 62px; top: 100px; font-size: 62px; letter-spacing: 2px; }
  .cta-button { position: absolute; left: 303px; top: 213px; width: 591px; height: 96px;
    border: 4px solid var(--white); border-radius: 48px; background: var(--green-dark);
    color: var(--white); font-size: 38px; letter-spacing: 1px;
    display: flex; align-items: center; justify-content: center; }

  .features { position: absolute; left: 0; top: 1060px; width: 1200px; height: 1166px;
    background: linear-gradient(180deg, #dfe7ed 0%, #eef2f5 100%); }
  .features-photo { position: absolute; right: 0; top: 0; width: 580px; height: 1166px;
    background: linear-gradient(90deg, rgba(238,242,245,0) 0%, #e9eef2 20%, #f4f6f8 60%, #dfe6ec 100%); }
  .features-title { position: absolute; left: 63px; top: 40px; font-size: 46px; color: var(--blue); }
  .features-intro { position: absolute; left: 63px; top: 108px; width: 545px;
    font-family: "Open Sans", Arial, sans-serif; font-size: 21px; line-height: 32px; color: #6b7077; text-align: justify; }
  .feature-list { position: absolute; left: 63px; top: 322px; list-style: none; }
  .feature { height: 111px; display: flex; align-items: center; gap: 22px; }
  .feature svg { width: 84px; height: 84px; flex: none; }
  .feature-label { color: var(--blue); text-transform: uppercase; line-height: 1.2; }
  .feature-label small { display: block; font-size: 19px; }
  .feature-label strong { display: block; font-weight: 400; font-size: 27px; }
</style>
</head>
<body>
  <header class="site-header">
    <a class="booking-slot">Slot Lantern</a>
    <div class="brand"><span class="brand-mark"></span><span class="brand-name">Harbour Lane GP</span></div>
    <div class="header-phone">
      <svg width="38" height="38" viewBox="0 0 24 24" fill="none" stroke="#8a9aa8" stroke-width="1.8"><path d="M5 3h4l2 5-2.5 1.5a11 11 0 0 0 6 6L16 13l5 2v4a2 2 0 0 1-2 2A17 17 0 0 1 3 5a2 2 0 0 1 2-2z"/></svg>
      <span>6210 4477</span>
    </div>
  </header>

  <nav class="nav-bar"><div class="menu-toggle"><span></span><span></span><span></span></div></nav>

  <div class="hero-visual" role="img" aria-label="Photo of a doctor's hand holding a stethoscope among glowing blue hexagon medical icons"></div>

  <section class="cta-band">
    <p class="cta-kicker">IF YOU NEED A DOCTOR ?</p>
    <h1 class="cta-title" style="font-weight:400">MAKE AN APPOINTMENT NOW !</h1>
    <a class="cta-button">GET AN APPOINTMENT</a>
  </section>

  <section class="features">
    <div class="features-photo" role="img" aria-label="Photo of a doctor in a white coat with a stethoscope holding a blue clipboard"></div>
    <h2 class="features-title" style="font-weight:400">What Makes Us Different</h2>
    <p class="features-intro">Lorem ipsum dolor sit amet, consectetur adipiscing elit. Sed vitae lectus pellentesque, condimentum leo ac, interdum orci. Morbi tristique ipsum nec convallis lobortis. Suspendisse justo nisi, dictum nec mattis eu, lobortis eget elit.</p>
    <ul class="feature-list">
      <li class="feature">
        <svg viewBox="0 0 40 40" fill="none" stroke="#1fa3e0" stroke-width="2.2"><circle cx="16" cy="15" r="7"/><path d="M4 36c0-7 5-11 12-11s12 4 12 11z"/><circle cx="31" cy="9" r="6"/><path d="M31 6v6M28 9h6"/></svg>
        <span class="feature-label"><small>Free</small><strong>Consultation</strong></span>
      </li>
      <li class="feature">
        <svg viewBox="0 0 40 40" fill="none" stroke="#1fa3e0" stroke-width="2.2"><circle cx="14" cy="14" r="6"/><circle cx="27" cy="12" r="5"/><path d="M3 34c0-6 5-10 11-10s11 4 11 10z"/><path d="M24 22c7-1 13 3 13 10h-9"/></svg>
        <span class="feature-label"><small>Qualified</small><strong>Doctors</strong></span>
      </li>
      <li class="feature">
        <svg viewBox="0 0 40 40" fill="none" stroke="#1fa3e0" stroke-width="2.2"><rect x="5" y="7" width="30" height="20" rx="1"/><path d="M3 32h34M15 27v5M25 27v5"/></svg>
        <span class="feature-label"><small>Professional</small><strong>Staff</strong></span>
      </li>
      <li class="feature">
        <svg viewBox="0 0 40 40" fill="none" stroke="#1fa3e0" stroke-width="2.2"><circle cx="20" cy="21" r="13"/><path d="M20 13v8l6 4M6 9l5-4M34 9l-5-4"/></svg>
        <span class="feature-label"><small>24x7</small><strong>Opened</strong></span>
      </li>
      <li class="feature">
        <svg viewBox="0 0 40 40" fill="none" stroke="#1fa3e0" stroke-width="2.2"><rect x="4" y="10" width="28" height="18" rx="2"/><path d="M4 15h28M8 23h8"/><path d="M10 10V6h26v18h-4"/></svg>
        <span class="feature-label"><small>Affordable</small><strong>Prices</strong></span>
      </li>
      <li class="feature">
        <svg viewBox="0 0 40 40" fill="none" stroke="#1fa3e0" stroke-width="2.2"><rect x="4" y="17" width="7" height="17"/><path d="M11 19l7-12c3 0 4 2 3 6l-1 4h11c2 0 3 2 2 4l-3 11c-1 2-2 2-4 2H11z"/></svg>
        <span class="feature-label"><small>~100000</small><strong>Happy Clients</strong></span>
      </li>
    </ul>
  </section>
</body>
</html>
```